Healthcare IT company looking for business card design

We develop IT systems for healthcare that significantly reduces cost and improves quality.

We want a business card design that is professional and clean, and using the colors in our logo.

Target Market(s)

Doctors and decision makers in the healthcare industry

Industry/Entity Type

Healthcare

Contact Information for Business Card

It should include
Name and title, address, telephone

Tobias Vrenholt, CEO
+46 712 418257
tobias@kelvaro.se

Font styles to use
Serif

Colors
0355a3
ed282f

Requirements
Must have
• Clean design
• Professional feel
Nice to have
• N/A
Should not have
• N/A

```html
<!DOCTYPE html>
<html lang="en">
<head>
<meta charset="utf-8">
<title>Kelvaro – Business Card</title>
<link rel="stylesheet" href="https://fonts.googleapis.com/css2?family=EB+Garamond:wght@400;700&display=swap">
<style>
  :root {
    --brand-blue: #0355a3;
    --card-blue: #1565b4;
    --brand-red: #ed282f;
    --card-white: #ffffff;
    --backdrop: #e9e6e1;
    --ink: #1f4f95;
  }
  * { margin: 0; padding: 0; box-sizing: border-box; }
  html, body {
    width: 1200px;
    height: 1023px;
    overflow: hidden;
    background: var(--backdrop);
  }
  .stage {
    position: relative;
    width: 1200px;
    height: 1023px;
  }
  .business-card {
    position: absolute;
    left: 100px;
    top: 231px;
    width: 1000px;
    height: 560px;
    background: var(--card-white);
    overflow: hidden;
    box-shadow: 0 10px 30px rgba(0,0,0,0.18);
  }
  .stripe-set {
    position: absolute;
    left: 0;
    top: 0;
    width: 1000px;
    height: 560px;
  }
  .brand {
    position: absolute;
    left: 90px;
    top: 190px;
    display: flex;
    align-items: flex-start;
    gap: 14px;
  }
  .brand-name {
    font-family: "EB Garamond", Georgia, serif;
    font-weight: 700;
    font-size: 118px;
    line-height: 1;
    color: var(--brand-blue);
    letter-spacing: 1px;
  }
  .brand-mark {
    width: 26px;
    height: 26px;
    margin-top: 14px;
    background: var(--brand-red);
  }
  .holder {
    position: absolute;
    left: 96px;
    top: 318px;
    font-family: "EB Garamond", Georgia, serif;
    font-size: 40px;
    color: var(--brand-red);
  }
  .contact-list {
    position: absolute;
    left: 700px;
    top: 200px;
    list-style: none;
  }
  .contact-item {
    display: flex;
    align-items: center;
    gap: 18px;
    margin-bottom: 14px;
    font-family: "EB Garamond", Georgia, serif;
    font-size: 31px;
    color: var(--ink);
  }
  .contact-icon {
    width: 40px;
    height: 40px;
    border-radius: 6px;
    background: var(--brand-red);
    display: flex;
    align-items: center;
    justify-content: center;
  }
</style>
</head>
<body>
<main class="stage">
  <section class="business-card" aria-label="Kelvaro business card, front">
    <svg class="stripe-set" viewBox="0 0 1000 560" aria-hidden="true">
      <rect x="430" y="0" width="570" height="24" fill="var(--card-blue)"/>
      <rect x="430" y="38" width="570" height="10" fill="var(--card-blue)"/>
      <rect x="430" y="62" width="570" height="30" fill="var(--card-blue)"/>
      <rect x="430" y="108" width="570" height="44" fill="var(--card-blue)"/>
      <rect x="280" y="420" width="520" height="140" fill="var(--card-blue)"/>
    </svg>

    <div class="brand">
      <span class="brand-name">Kelvaro</span>
      <span class="brand-mark" aria-hidden="true"></span>
    </div>
    <p class="holder">Tobias Vrenholt, CEO</p>

    <ul class="contact-list">
      <li class="contact-item">
        <span class="contact-icon" aria-hidden="true">
          <svg width="24" height="24" viewBox="0 0 24 24">
            <path d="M6.6 10.8a15 15 0 0 0 6.6 6.6l2.2-2.2a1 1 0 0 1 1-.25 11.4 11.4 0 0 0 3.6.57 1 1 0 0 1 1 1V20a1 1 0 0 1-1 1A17 17 0 0 1 3 4a1 1 0 0 1 1-1h3.5a1 1 0 0 1 1 1c0 1.25.2 2.45.57 3.57a1 1 0 0 1-.25 1z" fill="#fff"/>
          </svg>
        </span>
        +46 712 418257
      </li>
      <li class="contact-item">
        <span class="contact-icon" aria-hidden="true">
          <svg width="24" height="24" viewBox="0 0 24 24">
            <rect x="3" y="6" width="18" height="12" fill="#fff"/>
            <path d="M3 6l9 7 9-7" fill="none" stroke="var(--brand-red)" stroke-width="1.6"/>
          </svg>
        </span>
        tobias@kelvaro.se
      </li>
    </ul>
  </section>
</main>
</body>
</html>
```